"Landing Page Design for Premium Eco-Friendly Laundry Strips – Plooifris.nl"

We need a visually appealing and high-converting landing page for our premium laundry strips, emphasizing luxury, sustainability, and ease of use. The page should include sections such as:

Hero Section: A compelling introduction with a strong headline, subheadline, and a clear call-to-action (CTA).
Product Benefits: Highlighting key features like eco-friendliness, long-lasting scent, and hypoallergenic qualities.
Product Description: Focusing on innovation and sustainability.
How It Works: Simple, visual steps for using the product.
Customer Reviews: Authentic testimonials to build trust and social proof.
FAQ Section: Addressing common concerns about the product.
The design should maintain a luxurious aesthetic while ensuring clarity and user-friendliness. We also offer free shipping on all orders, a key differentiator to be prominently displayed. All texts and translations are already provided for implementation. Please deliver the design in Figma format."

Target Market(s)

"Eco-conscious consumers and families seeking premium and sustainable laundry solutions. Target age group: 25-50, predominantly women who prioritize luxury and environmental impact."

Industry/Entity Type

"Laundry care and eco-friendly consumer goods."

Coding

Requirements
Must have
• A visually luxurious design emphasizing premium quality and eco-friendliness. Clear call-to-actions (e.g., 'Try Now – Free Shipping'). Sections for product benefits, how it works, customer reviews, and FAQ. Highlight free shipping with no minimum order prominently."
Nice to have
• Elegant, minimalist animations to enhance the premium feel. Subtle use of gold and black to emphasize luxury, with a touch of green for sustainability. Interactive customer reviews section (e.g., carousel or testimonials)."
Should not have
• Overly cluttered designs or overwhelming text blocks. Generic stock photos not aligned with our brand identity. Bright or overly playful color schemes that detract from the premium feel."

```html
<!DOCTYPE html>
<html lang="nl">
<head>
<meta charset="utf-8">
<title>Plooifris – Premium Wasstrips</title>
<link rel="stylesheet" href="https://fonts.googleapis.com/css2?family=Jost:wght@500;600;700&family=Merriweather:wght@400;700&family=Arimo:wght@400;700&display=swap">
<style>
:root{
  --gold:#d8b13c;
  --gold-dark:#a87c1f;
  --gold-grad:linear-gradient(90deg,#a87c1f,#e2bf4f);
  --brown:#6e5020;
  --ink:#1b1b1b;
  --text:#333;
  --muted:#777;
  --cream:#f7edd2;
  --grey-bg:#f3f3f3;
  --white:#fff;
}
*{margin:0;padding:0;box-sizing:border-box}
html,body{width:1200px;height:4612px;overflow:hidden}
body{position:relative;background:var(--white);font-family:"Arimo",Arial,sans-serif;color:var(--text)}
.abs{position:absolute}
.serif{font-family:"Merriweather",Georgia,serif}
.label{position:absolute;left:0;width:1200px;text-align:center;font-size:15px;letter-spacing:.5px;color:#666;text-transform:uppercase}
.label::before,.label::after{content:"";display:inline-block;width:22px;height:2px;background:var(--gold);vertical-align:middle;margin:0 14px}
.heading{position:absolute;left:0;width:1200px;text-align:center;font-family:"Merriweather",Georgia,serif;font-weight:700;font-size:36px;color:var(--ink);line-height:1.2}
.btn-gold{position:absolute;background:var(--gold-grad);color:#fff;border-radius:8px;font-size:13px;display:flex;align-items:center;justify-content:center}

/* header */
.site-header{position:absolute;left:0;top:0;width:1200px;height:88px;background:#fff}
.brand{position:absolute;left:142px;top:28px;font-family:"Merriweather",serif;font-size:18px;color:var(--gold-dark);display:flex;align-items:center;gap:8px}
.brand i{width:14px;height:14px;border-radius:50%;background:var(--gold);display:block}
.contact-btn{left:882px;top:22px;width:112px;height:46px;border-radius:23px;background:var(--gold);color:var(--ink);font-family:"Jost",sans-serif;font-weight:500;font-size:14px}
.lang-btn{position:absolute;left:1014px;top:23px;width:44px;height:44px;border-radius:50%;border:2px solid var(--gold);display:flex;align-items:center;justify-content:center}

/* hero */
.hero{position:absolute;left:0;top:88px;width:1200px;height:620px;overflow:hidden}
.hero-photo{position:absolute;inset:0;background:linear-gradient(90deg,#2a2a2a 0%,#5a5a5a 35%,#cfcfcf 60%,#e9e9e9 75%,#bfb5a5 100%)}
.hero h1{position:absolute;left:141px;top:90px;width:480px;font-family:"Jost",sans-serif;font-weight:700;font-size:43px;line-height:1.35;color:#fff}
.hero p{position:absolute;left:141px;top:282px;width:470px;font-size:15px;line-height:2;color:#eee}
.hero .ship{left:141px;top:364px;width:176px;height:42px;border-radius:21px;background:var(--gold);color:#2a1e06;font-family:"Jost",sans-serif;font-size:13px;font-weight:500}

/* benefits */
.benefit{position:absolute;width:281px;height:210px;background:#fff;border-radius:12px;box-shadow:0 6px 22px rgba(0,0,0,.09);text-align:center}
.benefit-icon{position:absolute;top:-38px;left:88px;width:106px;height:106px;border-radius:26px;background:var(--cream)}
.benefit h3{margin-top:90px;font-family:"Jost",sans-serif;font-weight:500;font-size:17px;color:var(--ink)}
.benefit p{margin:14px 22px 0;font-size:13.5px;line-height:1.95;color:#333}

/* description */
.desc-media{left:142px;top:1553px;width:398px;height:362px;border-radius:60px;background:linear-gradient(135deg,#d9cfc4,#efe9e1 55%,#c9bca8)}
.desc-pack{left:412px;top:1790px;width:127px;height:127px;border-radius:10px;background:linear-gradient(135deg,#e0b844,#8a6214)}
.desc-label{position:absolute;left:640px;top:1610px;font-size:15px;color:#666;text-transform:uppercase}
.desc-label::before{content:"";display:inline-block;width:22px;height:2px;background:var(--gold);vertical-align:middle;margin-right:12px}
.desc h2{position:absolute;left:640px;top:1638px;width:420px;font-family:"Merriweather",serif;font-weight:700;font-size:35px;line-height:1.25;color:var(--ink)}
.desc p{position:absolute;left:640px;top:1730px;width:400px;font-size:13.5px;line-height:1.95;color:#222}

/* steps */
.step{position:absolute;width:108px;height:108px;border-radius:50%;background:var(--gold);display:flex;align-items:center;justify-content:center}
.step-num{position:absolute;font-family:"Merriweather",serif;font-size:30px;color:#d8d3c8}
.step-text{position:absolute;width:200px;text-align:center;font-family:"Merriweather",serif;font-size:13.5px;line-height:1.6;color:#222}
.shop-btn{left:483px;top:2505px;width:233px;height:40px;gap:30px}

/* reviews */
.reviews{position:absolute;left:0;top:2632px;width:1200px;height:540px;background:var(--grey-bg)}
.review{position:absolute;top:198px;width:437px;height:198px;background:#fff;border-radius:12px}
.stars{position:absolute;left:38px;top:22px;color:var(--gold);font-size:14px;letter-spacing:2px}
.review p{position:absolute;left:38px;top:52px;width:360px;font-size:14px;line-height:1.95;color:#333}
.avatar{position:absolute;left:42px;top:116px;width:64px;height:64px;border-radius:50%;background:linear-gradient(135deg,#c9b7a4,#8b7663)}
.reviewer{position:absolute;left:122px;top:138px;font-size:16px;color:var(--gold-dark)}
.quote{position:absolute;right:38px;top:100px;font-family:"Merriweather",serif;font-size:110px;line-height:1;color:#e3e3e3}
.arrow{position:absolute;width:50px;height:50px;border-radius:50%;display:flex;align-items:center;justify-content:center}
.dot{position:absolute;top:432px;width:14px;height:14px;border-radius:50%;border:1.5px solid var(--brown)}

/* faq */
.faq-blob{left:0;top:3480px;width:720px;height:330px;background:#f4e7c8;border-radius:0 60% 40% 0/0 70% 50% 0}
.faq-item{position:absolute;left:318px;width:564px;background:#fff;border:1.5px solid var(--gold);border-radius:4px}
.faq-item h4{position:absolute;left:36px;top:13px;font-family:"Merriweather",serif;font-size:12.5px;font-weight:700;color:#222}
.faq-item h4::before{content:"";position:absolute;left:-22px;top:5px;width:8px;height:8px;border:1.5px solid var(--gold);transform:rotate(45deg)}
.faq-item p{position:absolute;left:36px;top:42px;width:460px;font-size:11.5px;line-height:1.6;color:#444}
.faq-item .sign{position:absolute;right:18px;top:8px;font-size:20px;color:var(--brown)}

/* cta */
.cta{position:absolute;left:142px;top:3755px;width:917px;height:281px;border-radius:18px;overflow:hidden;background:linear-gradient(90deg,#000 0%,#0d0d0d 42%,#6b6256 62%,#d9d3c6 78%,#f09a2a 100%)}
.cta h2{position:absolute;left:0;top:42px;width:612px;text-align:center;font-family:"Merriweather",serif;font-weight:400;font-size:33px;line-height:1.28;color:#fff}
.cta .btn-gold{left:197px;top:194px;width:213px;height:38px}

/* footer */
.site-footer{position:absolute;left:0;top:4124px;width:1200px;height:488px;background:var(--brown)}
.foot-brand{position:absolute;left:0;top:160px;width:1200px;text-align:center;font-family:"Merriweather",serif;font-size:22px;color:var(--gold)}
.foot-mark{position:absolute;left:574px;top:90px;width:52px;height:52px;border-radius:50%;background:var(--gold)}
.foot-tag{position:absolute;left:0;top:228px;width:1200px;text-align:center;font-size:14px;color:#f2e6cc}
.foot-line{position:absolute;left:0;width:1200px;height:1px;background:rgba(255,255,255,.25)}
.contact{position:absolute;top:345px;display:flex;gap:24px;align-items:center;color:#f2e6cc;font-size:13px;line-height:1.7}
.contact-icon{width:58px;height:58px;border-radius:14px;background:#fff;display:flex;align-items:center;justify-content:center}
.copy{position:absolute;left:142px;top:452px;font-size:12px;color:#f2e6cc}
.social{position:absolute;top:446px;width:24px;height:24px;border-radius:50%;border:1.5px solid #f2e6cc}
</style>
</head>
<body>

<header class="site-header">
  <div class="brand"><i></i>Plooifris</div>
  <div class="btn-gold contact-btn">Contact Us</div>
  <div class="lang-btn">
    <svg width="26" height="26" viewBox="0 0 24 24" fill="none" stroke="#1b1b1b" stroke-width="1.5"><circle cx="12" cy="12" r="10"/><ellipse cx="12" cy="12" rx="4.5" ry="10"/><path d="M2 12h20M4 6.5h16M4 17.5h16"/></svg>
  </div>
</header>

<section class="hero">
  <div class="hero-photo" role="img" aria-label="Wasmachine met een mand vol opgevouwen handdoeken op een houten vloer voor een witte bakstenen muur"></div>
  <svg class="abs" style="left:0;top:420px" width="1200" height="200" viewBox="0 0 1200 200">
    <path d="M0 80 L0 200 L1200 200 L1200 70 L560 190 Z" fill="#fff"/>
    <path d="M0 60 L0 100 L560 185 L1200 60 L1200 40 L560 165 Z" fill="#d9b13b"/>
    <path d="M0 112 L560 200" stroke="#d9b13b" stroke-width="2"/>
    <path d="M560 200 L1200 80" stroke="#d9b13b" stroke-width="2"/>
  </svg>
  <h1>Experience Luxury And Sustainability in Every Wash</h1>
  <p>Discover Plooifris's premium laundry strips – where sophistication meets ecological consciousness.</p>
  <div class="btn-gold ship">Always Free Shipping!</div>
</section>

<section class="benefits">
  <div class="label" style="top:782px">Productvoordelen</div>
  <h2 class="heading" style="top:812px">Waarom Kiezen Voor<br>Plooifris Wasstrips?</h2>

  <div class="benefit" style="left:142px;top:970px"><div class="benefit-icon" role="img" aria-label="Icoon blad en druppel"></div><h3>Milieuvriendelijk</h3><p>100% biologisch afbreekbaar en plasticvrij.</p></div>
  <div class="benefit" style="left:464px;top:970px"><div class="benefit-icon" role="img" aria-label="Icoon wasmachine"></div><h3>Geschikt voor Alle Stoffen</h3><p>Veilig voor fijne was, wit, kleur en zwart.</p></div>
  <div class="benefit" style="left:777px;top:970px"><div class="benefit-icon" role="img" aria-label="Icoon handen met hart"></div><h3>Compact en Gebruiksvriendelijk</h3><p>Geen gedoe met zware flessen - scheur, voeg toe en geniet.</p></div>

  <div class="benefit" style="left:142px;top:1265px"><div class="benefit-icon" role="img" aria-label="Icoon frisse geur"></div><h3 style="font-weight:600">Langdurige Geur</h3><p>Een heerlijke frisse geur die dagenlang blijft hangen.</p></div>
  <div class="benefit" style="left:464px;top:1265px"><div class="benefit-icon" role="img" aria-label="Icoon handen met druppel"></div><h3 style="font-weight:600">Hypoallergeen</h3><p>Perfect voor de gevoelige huid en babykleding.</p></div>
  <div class="benefit" style="left:777px;top:1265px"><div class="benefit-icon" role="img" aria-label="Icoon bezorgbus gratis"></div><h3 style="font-weight:600">Altijd Gratis Verzending</h3><p>Geen minimale bestelhoeveelheid vereist.</p></div>
</section>

<section class="desc">
  <div class="abs desc-media" role="img" aria-label="Moeder en dochter doen samen de was bij een wasmachine"></div>
  <div class="abs desc-pack" role="img" aria-label="Gouden verpakking met wasstrips"></div>
  <div class="desc-label">Product beschrijving</div>
  <h2>De Toekomst van Wassen Is Hier</h2>
  <p>Onze Plooifris Wasstrips combineren innovatie met duurzaamheid. Met slechts één strip per wasbeurt geniet je van een schone en heerlijk geurende was, zonder het milieu te belasten. Geen plastic flessen, geen verspilling - alleen pure waskracht in een handige strip.</p>
</section>

<section class="steps">
  <div class="label" style="top:2010px">Hoe het werkt</div>
  <h2 class="heading" style="top:2040px;font-weight:400;font-size:34px">Zo Gebruik Je Wasstrips</h2>
  <svg class="abs" style="left:0;top:2070px" width="1200" height="320" viewBox="0 0 1200 320">
    <path d="M0 80 C20 240 120 290 190 300 C300 310 360 150 476 150 C600 150 640 290 713 260 C790 230 800 100 900 100 C1000 100 1060 190 1110 130 C1150 80 1180 30 1200 10" fill="none" stroke="#e9d9a6" stroke-width="1.5" stroke-dasharray="2 3"/>
  </svg>
  <div class="step" style="left:190px;top:2268px"><svg width="40" height="40" viewBox="0 0 24 24" fill="none" stroke="#1b1b1b" stroke-width="1.4"><rect x="4" y="3" width="11" height="16" rx="1"/><rect x="9" y="6" width="11" height="15" rx="1" fill="#d8b13c"/></svg></div>
  <div class="step-num" style="left:254px;top:2232px">01</div>
  <div class="step-text" style="left:144px;top:2405px">Scheur een wasstrip af</div>

  <div class="step" style="left:422px;top:2167px"><svg width="40" height="40" viewBox="0 0 24 24" fill="none" stroke="#1b1b1b" stroke-width="1.4"><rect x="3" y="3" width="18" height="18" rx="2"/><circle cx="12" cy="13" r="5"/><path d="M5 7h8"/></svg></div>
  <div class="step-num" style="left:543px;top:2202px">02</div>
  <div class="step-text" style="left:376px;top:2300px">Plaats de strip direct in de trommel, samen met je wasgoed</div>

  <div class="step" style="left:659px;top:2264px"><svg width="40" height="40" viewBox="0 0 24 24" fill="none" stroke="#1b1b1b" stroke-width="1.4"><rect x="4" y="2" width="16" height="20" rx="2"/><circle cx="12" cy="13" r="5"/><path d="M7 5.5h4M15 5.5h1"/></svg></div>
  <div class="step-num" style="left:782px;top:2294px">03</div>
  <div class="step-text" style="left:613px;top:2400px">Start de wasmachine en laat de wasstrip zijn werk doen</div>

  <div class="step" style="left:896px;top:2126px"><svg width="40" height="40" viewBox="0 0 24 24" fill="none" stroke="#1b1b1b" stroke-width="1.4"><path d="M8 3l-5 3 2 4 2-1v11h10V9l2 1 2-4-5-3c-1 2-2 3-4 3S9 5 8 3z"/></svg></div>
  <div class="step-num" style="left:1010px;top:2124px">04</div>
  <div class="step-text" style="left:850px;top:2260px">Geniet van perfect schone en fris ruikende kleding!</div>

  <div class="btn-gold shop-btn"><span>SHOP NU</span><span style="width:14px;height:14px;border:1.5px solid #fff;transform:rotate(45deg)"></span><span>Vanaf €14.95</span></div>
</section>

<section class="reviews">
  <div class="label" style="top:98px">Beoordelingen van klanten</div>
  <h2 class="heading" style="top:120px;font-weight:400;font-size:34px">Wat Onze Klanten Zeggen</h2>
  <div class="arrow" style="left:65px;top:273px;background:#f6ecd3"><svg width="16" height="16" viewBox="0 0 24 24" fill="none" stroke="#6e5020" stroke-width="2.5"><path d="M15 5l-7 7 7 7"/></svg></div>
  <div class="review" style="left:142px"><div class="stars">★★★★★</div><p>Eindelijk een milieuvriendelijk product dat echt werkt en heerlijk ruikt.</p><div class="avatar" role="img" aria-label="Portretfoto van klant"></div><div class="reviewer">Daan</div><div class="quote">”</div></div>
  <div class="review" style="left:621px"><div class="stars">★★★★★</div><p>Sinds ik Plooifris gebruik, voelt mijn was frisser en luxueuzer aan dan ooit.</p><div class="avatar" role="img" aria-label="Portretfoto van klant"></div><div class="reviewer">Lotte</div><div class="quote">”</div></div>
  <div class="arrow" style="left:1085px;top:273px;background:var(--brown)"><svg width="16" height="16" viewBox="0 0 24 24" fill="none" stroke="#fff" stroke-width="2.5"><path d="M9 5l7 7-7 7"/></svg></div>
  <div class="dot" style="left:563px"></div>
  <div class="dot" style="left:593px;background:radial-gradient(circle,var(--brown) 40%,#fff 45%)"></div>
  <div class="dot" style="left:623px"></div>
</section>

<section class="faq">
  <div class="abs faq-blob"></div>
  <div class="label" style="top:3262px">FAQ</div>
  <h2 class="heading" style="top:3290px;font-size:34px">Heb Je Nog Vragen?</h2>
  <div class="faq-item" style="top:3372px;height:100px"><h4>Zijn de wasstrips geschikt voor mensen met een gevoelige huid?</h4><p>Ja, onze wasstrips zijn hypoallergeen en dermatologisch getest, waardoor ze veilig zijn voor de gevoelige huid.</p><span class="sign">–</span></div>
  <div class="faq-item" style="top:3490px;height:42px"><h4>Hoeveel wasbeurten bevat één verpakking?</h4><span class="sign">+</span></div>
  <div class="faq-item" style="top:3546px;height:42px"><h4>Werken de strips bij lage temperaturen?</h4><span class="sign">+</span></div>
  <div class="btn-gold" style="left:466px;top:3632px;width:267px;height:40px;font-size:12px">Bekijk Onze FAQ Voor Meer Antwoorden</div>
</section>

<section class="cta">
  <div class="abs" style="left:640px;top:0;width:277px;height:281px" role="img" aria-label="Vrouw met een wasmand vol wasgoed"></div>
  <h2>Moeiteloos schoon, milieuvriendelijk gemak met wasstrips</h2>
  <div class="btn-gold">Bestel Nu - Maak Het Verschil!</div>
</section>

<footer class="site-footer">
  <div class="foot-mark"></div>
  <div class="foot-brand">PLOOIFRIS</div>
  <div class="foot-tag">Start Vandaag Met Milieuvriendelijk Wassen - Geen Plastic, Geen Gedoe. Alleen Fris Wassen.</div>
  <div class="foot-line" style="top:306px"></div>
  <div class="contact" style="left:200px"><div class="contact-icon"><svg width="30" height="30" viewBox="0 0 24 24" fill="var(--brown)"><path d="M12 2a7 7 0 0 0-7 7c0 5 7 13 7 13s7-8 7-13a7 7 0 0 0-7-7zm0 9.5A2.5 2.5 0 1 1 12 6.5a2.5 2.5 0 0 1 0 5z"/></svg></div><div>123, Building Name, Street<br>City, State XyY 123456</div></div>
  <div class="contact" style="left:534px"><div class="contact-icon"><svg width="30" height="30" viewBox="0 0 24 24" fill="var(--brown)"><path d="M6.6 10.8a15 15 0 0 0 6.6 6.6l2.2-2.2c.3-.3.7-.4 1-.2 1.1.4 2.3.6 3.6.6.6 0 1 .4 1 1V20c0 .6-.4 1-1 1A17 17 0 0 1 3 4c0-.6.4-1 1-1h3.5c.6 0 1 .4 1 1 0 1.3.2 2.5.6 3.6.1.3 0 .7-.2 1z"/></svg></div><div>Call Us<br>(123) 456 7890</div></div>
  <div class="contact" style="left:805px"><div class="contact-icon"><svg width="30" height="30" viewBox="0 0 24 24" fill="var(--brown)"><path d="M2 5h20v14H2z"/><path d="M2 5l10 8 10-8" stroke="#fff" stroke-width="1.6" fill="none"/></svg></div><div>Email Us<br>info@plooifris.nl</div></div>
  <div class="foot-line" style="top:430px"></div>
  <div class="copy">© 2024 Plooifris. Alle rechten voorbehouden.</div>
  <div class="social" style="left:975px"></div>
  <div class="social" style="left:1005px"></div>
  <div class="social" style="left:1035px"></div>
</footer>

</body>
</html>
```